Redesign of Website

We need an overhaul of our website. I've attached our current logo files. Please visit www.pelvorix.com for our current website for information about our company. We are looking for the same type of website (information-based only) so no need for any online store, payments, interactive stuff or anything like that...basically looking for a fresh new look! Also please make sure this design will be mobile-friendly. Thanks!

```html
<!DOCTYPE html>
<html lang="en">
<head>
<meta charset="utf-8">
<title>Veltmark Consultants, Inc.</title>
<link href="https://fonts.googleapis.com/css2?family=Poppins:wght@400;500;600;700&family=Mulish:wght@400;600;700;800&display=swap" rel="stylesheet">
<style>
:root{
  --blue:#0a4a94;
  --blue-dark:#063a78;
  --green:#5cb85c;
  --ink:#1c1c1c;
  --grey-text:#6d6d6d;
  --light:#efefef;
  --white:#ffffff;
  --dark:#1e2022;
  --black:#0b0b0b;
}
*{box-sizing:border-box;margin:0;padding:0}
html,body{width:1200px;height:3066px;overflow:hidden}
body{font-family:'Mulish',sans-serif;color:var(--ink);background:var(--white)}
.container{width:880px;margin:0 auto;position:relative}
section,header,footer{position:relative;width:1200px}

/* top bar */
.top-bar{height:45px;background:var(--blue);color:var(--white)}
.top-bar .container{display:flex;align-items:center;justify-content:space-between;height:45px}
.social-dots{display:flex;gap:12px}
.social-dots span{width:14px;height:14px;border-radius:50%;background:var(--white);display:block}
.top-contact{display:flex;align-items:center;gap:22px;font-size:13px}
.top-contact .item{display:flex;align-items:center;gap:8px}
.icon-ring{width:26px;height:26px;border-radius:50%;border:1.5px solid var(--white);display:flex;align-items:center;justify-content:center}

/* nav */
.site-nav{height:75px;background:var(--white);box-shadow:0 1px 4px rgba(0,0,0,.08)}
.site-nav .container{display:flex;align-items:center;justify-content:space-between;height:75px}
.brand{display:flex;align-items:center;gap:10px;font-family:'Poppins',sans-serif;font-weight:700;font-size:24px;color:var(--blue);letter-spacing:.5px}
.brand-mark{width:22px;height:22px;background:var(--blue)}
.menu{display:flex;gap:36px;font-family:'Poppins',sans-serif;font-size:13px;font-weight:500;color:var(--blue)}
.menu a{color:inherit;text-decoration:none;padding-bottom:6px}
.menu a.active{border-bottom:2px solid var(--blue)}

/* hero */
.hero{height:562px;text-align:center;color:var(--white);overflow:hidden}
.hero-photo{position:absolute;inset:0;background:linear-gradient(90deg,#2a2a26 0%,#4b4a42 35%,#3a3a36 65%,#56554c 100%)}
.hero-photo::after{content:"";position:absolute;inset:0;background:rgba(0,0,0,.35)}
.hero-content{position:relative;padding-top:170px}
.hero h1{font-family:'Poppins',sans-serif;font-weight:700;font-size:46px;color:var(--green);letter-spacing:.5px}
.hero p{font-size:19px;line-height:28px;margin:22px auto 0;width:640px}
.btn{display:inline-block;background:var(--blue);color:var(--white);font-family:'Poppins',sans-serif;font-weight:600;text-decoration:none;border-radius:3px}
.hero .btn{margin-top:26px;width:186px;height:51px;line-height:51px;font-size:17px}
.slider-dots{position:absolute;left:120px;top:284px;display:flex;flex-direction:column;align-items:center}
.slider-dots span{width:13px;height:13px;border-radius:50%;border:1.5px solid var(--white);margin:5px 0}
.slider-dots span.on{background:var(--white)}
.slider-dots i{width:1.5px;height:18px;background:var(--white)}

/* about */
.about{height:438px;text-align:center}
.eyebrow{font-family:'Poppins',sans-serif;font-weight:600;font-size:10px;letter-spacing:3px;color:var(--blue);text-transform:uppercase}
.about .eyebrow{padding-top:68px}
.section-title{font-family:'Poppins',sans-serif;font-weight:400;font-size:40px;color:var(--green);margin-top:4px}
.about h3{font-family:'Poppins',sans-serif;font-weight:500;font-size:20px;margin-top:20px}
.about p{font-size:12.5px;line-height:21px;color:var(--grey-text);text-align:left;margin-top:12px}
.about p + p{margin-top:20px}
.about .btn{margin-top:34px;width:112px;height:38px;line-height:38px;font-size:12px}

/* services */
.services{height:870px;overflow:hidden}
.services-photo{position:absolute;inset:0;background:linear-gradient(180deg,#1a58a8 0%,#134d99 55%,#0f4890 100%)}
.services-grid{position:absolute;left:162px;top:104px;display:grid;grid-template-columns:repeat(3,276px);grid-auto-rows:320px;column-gap:24px;row-gap:24px}
.intro-card{background:var(--green);color:var(--white);padding:28px 20px;position:relative}
.intro-card .eyebrow{color:var(--white)}
.intro-card h2{font-family:'Poppins',sans-serif;font-weight:400;font-size:40px;line-height:46px;margin-top:6px}
.intro-card .more{position:absolute;right:20px;bottom:24px;font-family:'Poppins',sans-serif;font-size:10px;font-weight:600;letter-spacing:.5px}
.service-card{background:var(--white);padding:40px 20px 0}
.service-card svg{display:block;width:76px;height:76px}
.service-card h4{font-family:'Poppins',sans-serif;font-weight:600;font-size:13px;margin-top:12px;line-height:18px;min-height:18px}
.service-card .rule{height:1px;background:#e2e2e2;margin:12px 0 14px}
.service-card p{font-size:12px;line-height:20px;color:var(--grey-text)}
.service-card .more{display:block;margin-top:14px;font-family:'Poppins',sans-serif;font-size:10px;font-weight:600;color:var(--blue)}

/* testimonials */
.testimonials{height:542px;background:var(--light);text-align:center}
.testimonials .eyebrow{padding-top:60px}
.quote-mark{font-family:'Poppins',sans-serif;font-weight:700;font-size:110px;line-height:80px;height:60px;margin-top:22px;color:var(--black)}
.testimonials blockquote{width:500px;margin:36px auto 0;font-size:12px;line-height:21px;color:var(--grey-text)}
.arrow{position:absolute;top:268px}
.arrow.prev{left:160px}
.arrow.next{right:158px}
.avatar{width:94px;height:94px;border-radius:50%;margin:26px auto 0;background:linear-gradient(160deg,#e6dcd2,#b9a797);border:3px solid var(--white)}
.client-name{font-family:'Poppins',sans-serif;font-weight:600;font-size:11px;color:var(--blue);margin-top:12px}

/* cta */
.cta{height:112px;background:var(--green)}
.cta .container{display:flex;align-items:center;justify-content:space-between;height:112px}
.cta h2{font-family:'Poppins',sans-serif;font-weight:600;font-size:26px;color:var(--white)}
.cta .btn{width:186px;height:52px;line-height:52px;text-align:center;font-size:17px}

/* contact */
.contact{height:378px;overflow:hidden}
.contact-photo{position:absolute;inset:0;background:linear-gradient(90deg,#202325 0%,#3a3c3d 50%,#2b2d2f 100%)}
.contact-photo::after{content:"";position:absolute;inset:0;background:rgba(0,0,0,.45)}
.contact .container{padding-top:40px}
.contact h2{font-family:'Poppins',sans-serif;font-weight:600;font-size:28px;color:var(--green)}
.contact-form{margin-top:18px;width:306px}
.field{background:var(--white);height:33px;margin-bottom:8px;font-size:10px;color:#555;padding:7px 6px;border-radius:2px}
.field.message{height:68px}
.contact-form .btn{margin-top:8px;width:90px;height:28px;line-height:28px;font-size:10px;text-align:center}
.contact-info{position:absolute;left:448px;top:150px;color:var(--white);font-size:11.5px}
.info-row{display:flex;gap:14px;align-items:flex-start;margin-bottom:20px;line-height:16px}
.info-row svg{flex:none;width:16px;height:16px}
.social-list{position:absolute;left:678px;top:140px;color:var(--white);font-size:11px}
.social-list li{list-style:none;display:flex;align-items:center;gap:12px;margin-bottom:10px}
.social-list .dot{width:30px;height:30px;border-radius:50%;background:var(--white)}
.social-list .dot.blue{background:#3b5998}

/* footer */
.site-footer{height:44px;background:var(--black);color:var(--white);text-align:center;font-size:12px;line-height:44px}
.site-footer strong{font-weight:800}
</style>
</head>
<body>

<header class="top-bar">
  <div class="container">
    <div class="social-dots"><span></span><span></span><span></span><span></span></div>
    <div class="top-contact">
      <div class="item"><span class="icon-ring"><svg width="14" height="10" viewBox="0 0 14 10"><rect x="0.5" y="0.5" width="13" height="9" fill="none" stroke="#fff"/><path d="M0.5 0.5 L7 6 L13.5 0.5" fill="none" stroke="#fff"/></svg></span>info@pelvorix.com</div>
      <div class="item"><span class="icon-ring"><svg width="12" height="12" viewBox="0 0 24 24"><path d="M6.6 10.8a15 15 0 006.6 6.6l2.2-2.2a1 1 0 011-.25 11.4 11.4 0 003.6.57 1 1 0 011 1V20a1 1 0 01-1 1A17 17 0 013 4a1 1 0 011-1h3.5a1 1 0 011 1 11.4 11.4 0 00.57 3.6 1 1 0 01-.25 1z" fill="#fff"/></svg></span>+1-555-014-2290</div>
    </div>
  </div>
</header>

<nav class="site-nav">
  <div class="container">
    <div class="brand"><span class="brand-mark"></span>Veltmark Consultants</div>
    <div class="menu"><a class="active" href="#">HOME</a><a href="#">ABOUT US</a><a href="#">SERVICES</a><a href="#">CONTACT US</a></div>
  </div>
</nav>

<section class="hero">
  <div class="hero-photo" role="img" aria-label="Modern office interior with plants and glass walls"></div>
  <div class="slider-dots"><span></span><span></span><i></i><span class="on"></span><span></span></div>
  <div class="hero-content">
    <h1>VELTMARK CONSULTANTS, INC.</h1>
    <p>Veltmark will give you the essential facts that are critical for solid business decision making and ongoing loan management.</p>
    <a class="btn" href="#">CONTACT US</a>
  </div>
</section>

<section class="about">
  <div class="container">
    <div class="eyebrow">About Us</div>
    <h2 class="section-title">Welcome To Veltmark Consultants</h2>
    <h3>Decades of Experience in Every Phase of Construction</h3>
    <p>Founded in 1990, Veltmark Consultants prides itself in providing customized, expert services to its clients. Our staff includes professionals who are credentialed and have years of real-world experience.</p>
    <p>We are committed to providing our clients with expert analysis of proposed and ongoing construction projects - providing crucial facts that will lead to lending decisions that end in success.</p>
    <a class="btn" href="#">READ MORE</a>
  </div>
</section>

<section class="services">
  <div class="services-photo" role="img" aria-label="City skyscrapers tinted blue"></div>
  <div class="services-grid">
    <div class="intro-card">
      <div class="eyebrow">Services</div>
      <h2>What We<br>Do?</h2>
      <span class="more">CONTACT US &rsaquo;</span>
    </div>
    <div class="service-card">
      <svg viewBox="0 0 76 76" fill="none" stroke="#5cb85c" stroke-width="2.5"><path d="M8 36 L38 10 L68 36"/><path d="M16 30 V66 H60 V30"/><rect x="30" y="46" width="16" height="20"/><path d="M38 38 c-4-5-10-1-6 4 l6 5 6-5 c4-5-2-9-6-4z"/><line x1="4" y1="66" x2="72" y2="66"/></svg>
      <h4>Property Condition Reports</h4>
      <div class="rule"></div>
      <p>Before moving ahead on any loan approval, financial institutions need to know the condition of existing structures.Our professional staff will give you the details...</p>
      <span class="more">READ MORE &rsaquo;</span>
    </div>
    <div class="service-card">
      <svg viewBox="0 0 76 76" fill="none" stroke="#5cb85c" stroke-width="2.5"><path d="M8 6 H38 V66 H8 Z"/><line x1="14" y1="16" x2="32" y2="16"/><line x1="14" y1="24" x2="32" y2="24"/><rect x="34" y="26" width="30" height="44"/><rect x="39" y="31" width="20" height="8"/><path d="M40 46h4M48 46h4M56 46h2M40 54h4M48 54h4M56 54h2M40 62h4M48 62h4M56 62h2"/></svg>
      <h4>Plan &amp; Cost Reviews</h4>
      <div class="rule"></div>
      <p>Our Plan &amp; Cost Reviews provide lending institutions with expert analysis of new construction projects before loan commitments are made...</p>
      <span class="more">READ MORE &rsaquo;</span>
    </div>
    <div class="service-card">
      <svg viewBox="0 0 76 76" fill="none" stroke="#5cb85c" stroke-width="2.5"><path d="M12 64 L44 32 M20 70 L50 40"/><path d="M44 32 a12 12 0 0 1 16-18 l-8 8 6 6 8-8 a12 12 0 0 1-18 16"/><path d="M14 10 L26 22 L22 26 L10 14 Z"/><path d="M26 22 L62 58 L58 62 L22 26"/></svg>
      <h4>Construction Funding Inspections</h4>
      <div class="rule"></div>
      <p>Lending institutions rarely have employees with the expertise needed to evaluate multiple stages of site construction and ensure that projects are being completed...</p>
      <span class="more">READ MORE &rsaquo;</span>
    </div>
    <div class="service-card">
      <svg viewBox="0 0 76 76" fill="none" stroke="#5cb85c" stroke-width="2.5"><path d="M38 6 L64 16 V36 C64 54 52 64 38 70 C24 64 12 54 12 36 V16 Z"/><circle cx="38" cy="38" r="16"/><path d="M32 44 c0-10 8-14 14-14 0 8-4 14-14 14z M30 46 l8-8"/></svg>
      <h4>Environmental Transaction Screens</h4>
      <div class="rule"></div>
      <p>Environmental Transaction Screens provide an economical but meaningful alternative for smaller properties such as mixed used buildings, multifamily...</p>
      <span class="more">READ MORE &rsaquo;</span>
    </div>
    <div class="service-card">
      <svg viewBox="0 0 76 76" fill="none" stroke="#5cb85c" stroke-width="2.5"><circle cx="38" cy="38" r="32"/><path d="M46 26 c-2-4-14-5-15 2 c-1 8 16 5 15 13 c-1 8-14 7-17 2"/><line x1="38" y1="16" x2="38" y2="60"/></svg>
      <h4>Phase 1 Environmental Site Assessment</h4>
      <div class="rule"></div>
      <p>With reasonable pricing and a quick turnaround, Veltmark provides comprehensive Phase 1 reports. Veltmark's reports provide a clear conclusion and definitive...</p>
      <span class="more">READ MORE &rsaquo;</span>
    </div>
  </div>
</section>

<section class="testimonials">
  <div class="eyebrow">Testimonials</div>
  <h2 class="section-title">What Our Clients Says</h2>
  <div class="quote-mark">&ldquo;</div>
  <blockquote>" Lorem Ipsum is simply dummy text of the printing and typesetting industry. Lorem Ipsum has been the industry's standard dummy text ever since the 1500s, when an unknown printer took a galley of type and scrambled it to make a type specimen book. "</blockquote>
  <svg class="arrow prev" width="34" height="20" viewBox="0 0 34 20" fill="none" stroke="#111" stroke-width="2.2"><path d="M33 10H2M10 2L2 10l8 8"/></svg>
  <svg class="arrow next" width="34" height="20" viewBox="0 0 34 20" fill="none" stroke="#111" stroke-width="2.2"><path d="M1 10h31M24 2l8 8-8 8"/></svg>
  <div class="avatar" role="img" aria-label="Client portrait photo"></div>
  <div class="client-name">~ CLIENT NAME</div>
</section>

<section class="cta">
  <div class="container">
    <h2>The Intelligent Choice For Every Business</h2>
    <a class="btn" href="#">CONTACT US</a>
  </div>
</section>

<section class="contact">
  <div class="contact-photo" role="img" aria-label="Team working together in an office"></div>
  <div class="container">
    <h2>CONTACT US</h2>
    <div class="contact-form">
      <div class="field">Name:</div>
      <div class="field">Email:</div>
      <div class="field">Phone:</div>
      <div class="field message">Message:</div>
      <a class="btn" href="#">SUBMIT</a>
    </div>
    <div class="contact-info">
      <div class="info-row"><svg viewBox="0 0 24 24"><path d="M6.6 10.8a15 15 0 006.6 6.6l2.2-2.2a1 1 0 011-.25 11.4 11.4 0 003.6.57 1 1 0 011 1V20a1 1 0 01-1 1A17 17 0 013 4a1 1 0 011-1h3.5a1 1 0 011 1 11.4 11.4 0 00.57 3.6 1 1 0 01-.25 1z" fill="none" stroke="#5cb85c" stroke-width="2"/></svg>+1-555-014-2290</div>
      <div class="info-row"><svg viewBox="0 0 16 16"><rect x="1" y="3" width="14" height="10" fill="none" stroke="#5cb85c" stroke-width="1.3"/><path d="M1 3l7 6 7-6" fill="none" stroke="#5cb85c" stroke-width="1.3"/></svg>info@pelvorix.com</div>
      <div class="info-row"><svg viewBox="0 0 16 16"><path d="M8 15s5-5.5 5-9A5 5 0 003 6c0 3.5 5 9 5 9z" fill="none" stroke="#5cb85c" stroke-width="1.3"/><circle cx="8" cy="6" r="1.8" fill="none" stroke="#5cb85c" stroke-width="1.3"/></svg><span>418 Harlow Ave, Suite 12<br>Brenton Township, NJ-07000</span></div>
    </div>
    <ul class="social-list">
      <li><span class="dot blue"></span>Network</li>
      <li><span class="dot"></span>Careers</li>
      <li><span class="dot"></span>Updates</li>
      <li><span class="dot"></span>Gallery</li>
    </ul>
  </div>
</section>

<footer class="site-footer">&copy;2019 <strong>Veltmark Consultants INC.</strong> All Right Reserved. | Terms &amp; Conditions.</footer>

</body>
</html>
```